Dental Medical History Form - Content provided

Design a medical history form for a dental practice. Content is provided so all that is needed is the formatting to make it look great and easy to read.

"Patient Information" to include all information contained in top portion of the "Patient Medical History Form" docx file.

"Medical History" should follow the formatting and content of the "Exact Medical History" file as this is what the entry fields look like in our practice software and so we would like it to match.

1st page - Patient info, allergies, medications, antibiotics, joint replacement, pregnancy.

2nd page - Do you have, or have you had, any of the following? . . . . . . .

Target Market(s)

All ages but must be clear enough for elderly to read. Use as much space as possible to keep font size bigger yet keep to two pages

Industry/Entity Type

Dental

Font styles to use
Sans Serif

Requirements
Must have
• All content provided
• Our logo at the top (file provided)
• Century Gothic Font
• Limit to two pages

```html
<!DOCTYPE html>
<html lang="en">
<head>
<meta charset="utf-8">
<title>Lumen Dental – Confidential Medical History</title>
<link href="https://fonts.googleapis.com/css2?family=Questrial&display=swap" rel="stylesheet">
<style>
:root{
  --band:#58595b;
  --ink:#3e3f41;
  --soft:#5c5d60;
  --box:#86878a;
  --paper:#ffffff;
  --canvas:#ffffff;
  --edge:#e2e2e2;
}
*{box-sizing:border-box;margin:0;padding:0}
html,body{width:1200px;height:816px;overflow:hidden;background:var(--canvas)}
body{font-family:"Questrial","Century Gothic",sans-serif;color:var(--ink);position:relative}
.page{position:absolute;top:29px;width:538px;height:759px;background:var(--paper);border:1px solid var(--edge)}
.page--front{left:43px}
.page--back{left:618px}
.page *{position:absolute}
.page .flow, .page .flow *{position:static}

.brand{left:21px;top:14px;color:var(--soft);line-height:1}
.brand-name{font-size:35px;letter-spacing:.5px;position:static;display:block}
.brand-sub{font-size:14px;position:static;display:block;text-align:right;margin-top:-2px;letter-spacing:.5px}
.brand-dot{left:148px;top:4px;width:10px;height:10px;border-radius:50%;background:var(--box)}
.practice-address{right:20px;top:15px;text-align:right;font-size:10px;line-height:12px;color:var(--ink)}
.form-title{left:0;width:100%;top:71px;text-align:center;font-size:16.5px;letter-spacing:2px;color:var(--soft)}

.band{left:0;width:100%;height:16px;background:var(--band);color:#fff;font-size:9.5px;text-align:center;line-height:16px}
.band--head{top:0;height:19px;font-size:12.5px;line-height:19px;letter-spacing:.3px}

.label{font-size:9.5px;white-space:nowrap;line-height:12px}
.col-head{font-size:9.5px;text-align:center;line-height:12px}
.field{height:12px;border:1px solid var(--box);background:#fff}
.cell{width:12px;height:12px;border:1px solid var(--box)}
.tick{width:11px;height:11px;border:1px solid var(--box)}
.rule{height:1px;background:var(--box)}

.turn-tab{left:205px;width:128px;height:19px;top:740px;background:var(--band);border-radius:6px 6px 0 0;color:#fff;font-size:11px;text-align:center;line-height:21px}
.foot-band{left:0;width:100%;top:751px;height:8px;background:var(--band)}

.checklist{top:47px;width:230px}
.checklist--left{left:26px}
.checklist--right{left:307px}
.checklist .row{display:flex;align-items:center;height:17.2px}
.checklist .row .tick{position:static;flex:none}
.checklist .row span{font-size:9.5px;margin-left:19px}
.checklist .tag{display:inline-block;background:var(--band);color:#fff;font-size:9px;line-height:10px;height:10px;padding:0 4px;width:46px;margin-left:26px}
.checklist .tag--wide{width:84px}
.checklist--right .tag{margin-left:27px;width:44px}

.signoff{font-size:11.5px}
.thanks{left:0;width:100%;text-align:center;font-size:8px;line-height:13px;top:713px}
</style>
</head>
<body>

<section class="page page--front" aria-label="Page one: patient information">
  <div class="brand"><span class="brand-name">Lumen</span><span class="brand-sub">dental</span></div>
  <div class="practice-address">3.04/118 Harbour View Rd<br>Coralton NSW 2261<br>(02) 45 210 388</div>
  <h1 class="form-title" style="font-weight:400">CONFIDENTIAL MEDICAL HISTORY</h1>

  <div class="band" style="top:104px">General Information</div>

  <div class="col-head" style="left:59px;width:40px;top:130px">Title</div>
  <div class="col-head" style="left:106px;width:130px;top:130px">First</div>
  <div class="col-head" style="left:244px;width:130px;top:130px">Last</div>
  <div class="col-head" style="left:382px;width:130px;top:130px">Preferred</div>
  <div class="label" style="left:25px;top:144px">Name:</div>
  <div class="field" style="left:59px;top:144px;width:40px"></div>
  <div class="field" style="left:106px;top:144px;width:130px"></div>
  <div class="field" style="left:244px;top:144px;width:130px"></div>
  <div class="field" style="left:382px;top:144px;width:130px"></div>

  <div class="label" style="left:25px;top:169px">Address:</div>
  <div class="field" style="left:70px;top:169px;width:442px"></div>

  <div class="label" style="left:25px;top:194px">Email Address:</div>
  <div class="field" style="left:95px;top:194px;width:269px"></div>
  <div class="label" style="left:369px;top:194px">DOB:</div>
  <div class="cell" style="left:398px;top:194px"></div><div class="cell" style="left:411px;top:194px"></div>
  <div class="cell" style="left:429px;top:194px"></div><div class="cell" style="left:442px;top:194px"></div>
  <div class="cell" style="left:460px;top:194px"></div><div class="cell" style="left:473px;top:194px"></div>
  <div class="cell" style="left:486px;top:194px"></div><div class="cell" style="left:499px;top:194px"></div>

  <div class="label" style="left:25px;top:219px">Mobile</div>
  <div class="field" style="left:60px;top:219px;width:128px"></div>
  <div class="label" style="left:195px;top:219px">Work</div>
  <div class="field" style="left:222px;top:219px;width:128px"></div>
  <div class="label" style="left:354px;top:219px">Home</div>
  <div class="field" style="left:384px;top:219px;width:128px"></div>

  <div class="label" style="left:25px;top:244px">Emergency Contact Person:</div>
  <div class="field" style="left:150px;top:244px;width:362px"></div>

  <div class="label" style="left:25px;top:269px">Emergency Contact Relationship:</div>
  <div class="field" style="left:174px;top:269px;width:147px"></div>
  <div class="label" style="left:325px;top:269px">Phone:</div>
  <div class="field" style="left:360px;top:269px;width:152px"></div>

  <div class="label" style="left:25px;top:295px">General Practitioner Name:</div>
  <div class="field" style="left:150px;top:295px;width:196px"></div>
  <div class="label" style="left:350px;top:295px">Phone:</div>
  <div class="field" style="left:385px;top:295px;width:127px"></div>

  <div class="label" style="left:25px;top:320px">General Practitioner Address:</div>
  <div class="field" style="left:159px;top:320px;width:353px"></div>

  <div class="label" style="left:25px;top:345px">Do you have dental health fund cover?</div>
  <div class="tick" style="left:200px;top:345px"></div>
  <div class="label" style="left:215px;top:345px">Yes</div>
  <div class="tick" style="left:233px;top:345px"></div>
  <div class="label" style="left:251px;top:345px">No</div>
  <div class="label" style="left:270px;top:345px">If so, Name of Fund:</div>
  <div class="field" style="left:358px;top:345px;width:154px"></div>

  <div class="label" style="left:25px;top:370px">Fund Number:</div>
  <div class="field" style="left:88px;top:370px;width:182px"></div>
  <div class="label" style="left:278px;top:370px">Priority Number on card:1</div>
  <div class="cell" style="left:392px;top:370px"></div><div class="label" style="left:406px;top:370px">2</div>
  <div class="cell" style="left:414px;top:370px"></div><div class="label" style="left:427px;top:370px">3</div>
  <div class="cell" style="left:435px;top:370px"></div><div class="label" style="left:449px;top:370px">4</div>
  <div class="cell" style="left:457px;top:370px"></div><div class="label" style="left:470px;top:370px">5</div>
  <div class="cell" style="left:478px;top:370px"></div><div class="label" style="left:492px;top:370px">6</div>
  <div class="cell" style="left:500px;top:370px"></div>

  <div class="label" style="left:25px;top:396px">Occupation:</div>
  <div class="field" style="left:85px;top:396px;width:185px"></div>
  <div class="label" style="left:276px;top:396px">Referred by:</div>
  <div class="field" style="left:336px;top:396px;width:176px"></div>

  <div class="band" style="top:415px">Please indicate if you are allergic to any of the following ?</div>
  <div class="tick" style="left:26px;top:446px"></div><div class="label" style="left:43px;top:446px">Codeine</div>
  <div class="tick" style="left:96px;top:446px"></div><div class="label" style="left:113px;top:446px">Penicillin</div>
  <div class="tick" style="left:166px;top:446px"></div><div class="label" style="left:183px;top:446px">Sulphites</div>
  <div class="tick" style="left:236px;top:446px"></div><div class="label" style="left:253px;top:446px">Latex</div>
  <div class="tick" style="left:288px;top:446px"></div><div class="label" style="left:305px;top:446px">Local Anaesthetic</div>
  <div class="tick" style="left:402px;top:446px"></div><div class="label" style="left:419px;top:446px">Lactose</div>
  <div class="tick" style="left:470px;top:446px"></div><div class="label" style="left:487px;top:446px">Metal</div>
  <div class="label" style="left:25px;top:471px">Other:</div>
  <div class="field" style="left:60px;top:471px;width:452px"></div>

  <div class="band" style="top:497px">Are you currently taking, or have ever taken, any of the following medication ?</div>
  <div class="tick" style="left:26px;top:524px"></div><div class="label" style="left:43px;top:524px">Asthma inhaler</div>
  <div class="tick" style="left:120px;top:524px"></div><div class="label" style="left:138px;top:524px">Anti-epileptics</div>
  <div class="tick" style="left:210px;top:524px"></div><div class="label" style="left:227px;top:524px">Anti-depressants</div>
  <div class="tick" style="left:309px;top:524px"></div><div class="label" style="left:328px;top:524px">Blood Pressure</div>
  <div class="tick" style="left:399px;top:524px"></div><div class="label" style="left:418px;top:524px">Blood Thinners</div>
  <div class="tick" style="left:26px;top:549px"></div><div class="label" style="left:43px;top:549px">Bisphosphonates</div>
  <div class="tick" style="left:120px;top:549px"></div><div class="label" style="left:139px;top:549px">Chemotherapy</div>
  <div class="tick" style="left:210px;top:549px"></div><div class="label" style="left:227px;top:549px">Insulin</div>
  <div class="tick" style="left:268px;top:549px"></div><div class="label" style="left:288px;top:549px">Immunosuppressants</div>
  <div class="tick" style="left:389px;top:549px"></div><div class="label" style="left:410px;top:549px">Steroids</div>
  <div class="tick" style="left:455px;top:549px"></div><div class="label" style="left:479px;top:549px">Other</div>

  <div class="band" style="top:578px">Please specify medication name, dose, and frequency where possible:</div>
  <div class="rule" style="left:25px;top:607px;width:158px"></div><div class="rule" style="left:189px;top:607px;width:158px"></div><div class="rule" style="left:353px;top:607px;width:158px"></div>
  <div class="rule" style="left:25px;top:628px;width:158px"></div><div class="rule" style="left:189px;top:628px;width:158px"></div><div class="rule" style="left:353px;top:628px;width:158px"></div>
  <div class="rule" style="left:25px;top:649px;width:158px"></div><div class="rule" style="left:189px;top:649px;width:158px"></div><div class="rule" style="left:353px;top:649px;width:158px"></div>

  <div class="label" style="left:25px;top:663px">Do you require antibiotic cover?</div>
  <div class="tick" style="left:189px;top:663px"></div><div class="label" style="left:214px;top:663px">Yes</div>
  <div class="tick" style="left:245px;top:663px"></div><div class="label" style="left:274px;top:663px">No</div>

  <div class="label" style="left:25px;top:685px">Have you had a joint replacement?</div>
  <div class="tick" style="left:189px;top:685px"></div><div class="label" style="left:214px;top:685px">Yes</div>
  <div class="tick" style="left:245px;top:685px"></div><div class="label" style="left:274px;top:685px">No</div>

  <div class="label" style="left:25px;top:708px">Women:&nbsp; Are you pregnant?</div>
  <div class="tick" style="left:189px;top:708px"></div><div class="label" style="left:214px;top:708px">Yes</div>
  <div class="tick" style="left:245px;top:708px"></div><div class="label" style="left:274px;top:708px">No</div>
  <div class="tick" style="left:302px;top:708px"></div><div class="label" style="left:322px;top:708px">Possible</div>
  <div class="tick" style="left:375px;top:708px"></div><div class="tick" style="left:392px;top:708px"></div>
  <div class="label" style="left:418px;top:708px">How Many Weeks?</div>

  <div class="foot-band"></div>
  <div class="turn-tab">Please Turn Over</div>
</section>

<section class="page page--back" aria-label="Page two: medical conditions">
  <div class="band band--head">Do you have, or have you had, any of the following?</div>

  <div class="checklist checklist--left">
    <div class="flow">
      <div class="row"><span class="tag" style="margin-left:26px">Dental</span></div>
      <div class="row"><i class="tick"></i><span>Acid Reflux</span></div>
      <div class="row"><i class="tick"></i><span>Bad Breath/Taste</span></div>
      <div class="row"><i class="tick"></i><span>Bleeding/Swollen/Sore Gums</span></div>
      <div class="row"><i class="tick"></i><span>Blisters/Ulcers in Mouth</span></div>
      <div class="row"><i class="tick"></i><span>Broken tooth</span></div>
      <div class="row"><i class="tick"></i><span>Dry mouth</span></div>
      <div class="row"><i class="tick"></i><span>Food collection between teeth</span></div>
      <div class="row"><i class="tick"></i><span>Grinding teeth</span></div>
      <div class="row"><i class="tick"></i><span>Loose teeth</span></div>
      <div class="row"><i class="tick"></i><span>Crowded teeth</span></div>
      <div class="row"><i class="tick"></i><span>Discoloured teeth</span></div>
      <div class="row"><i class="tick"></i><span>Sensitivity to hot or cold</span></div>
      <div class="row"><i class="tick"></i><span>Tooth pain when chewing</span></div>
      <div class="row"><i class="tick"></i><span>Jaw Pain</span></div>
      <div class="row"><i class="tick"></i><span>Jaw Fracture</span></div>
      <div class="row"><i class="tick"></i><span>Oral Cancer</span></div>
      <div class="row"><span class="tag tag--wide" style="width:64px">Diet/Lifestyle</span></div>
      <div class="row"><i class="tick"></i><span>Drink more than one glass alcohol per day</span></div>
      <div class="row"><i class="tick"></i><span>Smoking</span></div>
      <div class="row"><i class="tick"></i><span>Carbonated drinks</span></div>
      <div class="row"><i class="tick"></i><span>Sugary foods</span></div>
      <div class="row"><span class="tag" style="width:63px">Blood</span></div>
      <div class="row"><i class="tick"></i><span>Anaemia</span></div>
      <div class="row"><i class="tick"></i><span>Leukemia</span></div>
      <div class="row"><i class="tick"></i><span>Low platelets</span></div>
      <div class="row"><span class="tag" style="width:63px">Chest</span></div>
      <div class="row"><i class="tick"></i><span>Bronchitis</span></div>
      <div class="row"><i class="tick"></i><span>Emphysema</span></div>
      <div class="row"><span class="tag tag--wide">Infectious Disease</span></div>
      <div class="row"><i class="tick"></i><span>Hepatitis A,B,C,D</span></div>
      <div class="row"><i class="tick"></i><span>HIV/AIDS</span></div>
      <div class="row"><i class="tick"></i><span>Tuberculosis</span></div>
    </div>
  </div>

  <div class="checklist checklist--right">
    <div class="flow">
      <div class="row"><span class="tag">Heart</span></div>
      <div class="row"><i class="tick"></i><span>Angina</span></div>
      <div class="row"><i class="tick"></i><span>Atrial Fibrillation</span></div>
      <div class="row"><i class="tick"></i><span>Congenital Heart Disease</span></div>
      <div class="row"><i class="tick"></i><span>Heart attack</span></div>
      <div class="row"><i class="tick"></i><span>Heart murmur</span></div>
      <div class="row"><i class="tick"></i><span>Heart surgery</span></div>
      <div class="row"><i class="tick"></i><span>Heart valve replacement</span></div>
      <div class="row"><i class="tick"></i><span>Infective endocarditis</span></div>
      <div class="row"><i class="tick"></i><span>Rheumatic Heart Disease</span></div>
      <div class="row"><i class="tick"></i><span>Pacemaker</span></div>
      <div class="row"><i class="tick"></i><span>Stent</span></div>
      <div class="row"><span class="tag">Other</span></div>
      <div class="row"><i class="tick"></i><span>Anxiety</span></div>
      <div class="row"><i class="tick"></i><span>Alzheimer's</span></div>
      <div class="row"><i class="tick"></i><span>Asthma</span></div>
      <div class="row"><i class="tick"></i><span>Anaphylaxis</span></div>
      <div class="row"><i class="tick"></i><span>Auto-immune disease</span></div>
      <div class="row"><i class="tick"></i><span>Blood Pressure</span></div>
      <div class="row"><i class="tick"></i><span>Depression</span></div>
      <div class="row"><i class="tick"></i><span>Diabetes</span></div>
      <div class="row"><i class="tick"></i><span>Epilepsy</span></div>
      <div class="row"><i class="tick"></i><span>Kidney Disease</span></div>
      <div class="row"><i class="tick"></i><span>Liver Disease</span></div>
      <div class="row"><i class="tick"></i><span>Osteoporosis</span></div>
      <div class="row"><i class="tick"></i><span>Radiation to Head/Neck</span></div>
    </div>
  </div>

  <div class="label" style="left:297px;top:507px;font-size:8px">Please list any other conditions we should be aware of:</div>
  <div class="field" style="left:297px;top:523px;width:211px;height:13px"></div>
  <div class="field" style="left:297px;top:544px;width:211px;height:13px"></div>
  <div class="field" style="left:297px;top:565px;width:211px;height:13px"></div>
  <div class="field" style="left:297px;top:585px;width:211px;height:13px"></div>
  <div class="field" style="left:297px;top:606px;width:211px;height:13px"></div>

  <div class="label signoff" style="left:28px;top:671px">Signature:</div>
  <div class="rule" style="left:83px;top:680px;width:197px;background:var(--ink)"></div>
  <div class="label signoff" style="left:297px;top:671px">Date:</div>
  <div class="rule" style="left:330px;top:680px;width:180px;background:var(--ink)"></div>

  <p class="thanks">Thank you for the time to complete your medical history form.<br>Oral health is linked to overall health and this comprehensive questionnaire will help us to provide you with optimal and safe care.</p>

  <div class="foot-band"></div>
  <div class="turn-tab" style="top:745px;height:14px"></div>
</section>

</body>
</html>
```